Business Card Design Project Calbrook Foundation

Looking for business card options to match our concurrent logo project on pixel forum. We are a international humanitarian aid firm. We work in the non profit sector but operate more closely to a traditional for-profit investment firm. As such we would like equal tones in our branding materials, which includes are business cards.

Stand by for logo...
Updates

logo uploaded.

Target Market(s)

Adults in western speaking countries ages 18-40 that work primarily in the NGO and Business Administrative Career Field.

Industry/Entity Type

Non Profit

Font styles to use
Sans Serif

Requirements
Nice to have
• We would like all contact information on one side.

Company Name/Logo, Individual Name and Position on the other...

```html
<!DOCTYPE html>
<html lang="en">
<head>
<meta charset="utf-8">
<title>Calbrook Foundation – Business Card</title>
<link href="https://fonts.googleapis.com/css2?family=Merriweather:ital,wght@0,400;0,700;1,400&display=swap" rel="stylesheet">
<style>
  :root {
    --page: #e9e9e7;
    --card-light: #ffffff;
    --card-dark: #333333;
    --ink: #3a3a3a;
    --ink-soft: #8a8a8a;
    --accent: #2f7fc6;
    --accent-pale: #dde7f5;
    --mark-grey: #5a5a5a;
  }
  * { box-sizing: border-box; margin: 0; padding: 0; }
  html, body {
    width: 1200px; height: 873px; overflow: hidden;
    background: var(--page);
    font-family: "Merriweather", Georgia, serif;
  }
  .sheet {
    width: 1200px; height: 873px;
    display: flex; align-items: center; justify-content: center; gap: 60px;
  }
  .card {
    width: 540px; height: 309px; position: relative; overflow: hidden;
    box-shadow: 0 6px 18px rgba(0,0,0,.12);
  }
  /* Front: person and contact */
  .card--front { background: var(--card-light); color: var(--ink); }
  .front__tint {
    position: absolute; left: 40px; top: 34px; width: 150px; height: 120px;
    background: var(--accent-pale); opacity: .55; border-radius: 6px;
  }
  .person { position: absolute; left: 70px; top: 70px; }
  .person__name { font-weight: 700; font-size: 17px; letter-spacing: .02em; }
  .person__role { font-style: italic; font-size: 12px; color: var(--ink-soft); margin-top: 6px; }
  .rule {
    position: absolute; left: 200px; top: 168px; width: 170px; height: 3px;
    background: linear-gradient(90deg, transparent, var(--accent) 70%, var(--accent-pale));
    border-radius: 2px;
  }
  .contact {
    position: absolute; left: 250px; top: 186px; list-style: none;
    font-size: 12.5px; color: var(--ink-soft);
  }
  .contact li { display: flex; align-items: center; gap: 12px; height: 21px; }
  .contact svg { width: 12px; height: 12px; flex: none; fill: var(--accent); }
  /* Back: organisation name */
  .card--back {
    background: var(--card-dark);
    display: flex; align-items: center; justify-content: center; gap: 16px;
  }
  .org__square { width: 34px; height: 34px; background: var(--accent); }
  .org__name { font-size: 26px; font-weight: 700; color: #1d1d1d; letter-spacing: .03em; }
</style>
</head>
<body>
<main class="sheet">
  <section class="card card--front" aria-label="Card front">
    <div class="front__tint"></div>
    <div class="person">
      <p class="person__name">DANIEL REYES</p>
      <p class="person__role">Managing Director</p>
    </div>
    <div class="rule"></div>
    <ul class="contact">
      <li><svg viewBox="0 0 12 12"><rect x="3" y="0" width="6" height="12" rx="1"/></svg>+123 555 0148</li>
      <li><svg viewBox="0 0 12 12"><rect x="0" y="2" width="12" height="8" rx="1"/></svg>danielreyes@mail.com</li>
      <li><svg viewBox="0 0 12 12"><circle cx="6" cy="6" r="6"/></svg>www.calbrook.org</li>
      <li><svg viewBox="0 0 12 12"><circle cx="6" cy="6" r="5"/></svg>www.chirpline.com</li>
      <li><svg viewBox="0 0 12 12"><rect x="1" y="1" width="10" height="10"/></svg>www.linkhub.com</li>
    </ul>
  </section>
  <section class="card card--back" aria-label="Card back">
    <span class="org__square"></span>
    <span class="org__name">Calbrook Foundation</span>
  </section>
</main>
</body>
</html>
```